Velmora Grove Club Postcard Design

Need a postcard for this business. Go to velmoragroveclub.com to see the product we are selling. Here's another good postcard you can sample. https://www.rowanpilsbydesign.com/?lightbox=dataItem-qz4tunal
Another one: http://blog.tranquet.com/postcard-examples-from-popular-startups/

```html
<!DOCTYPE html>
<html lang="en">
<head>
<meta charset="utf-8">
<title>Velmora Grove Club Postcard</title>
<link rel="stylesheet" href="https://fonts.googleapis.com/css2?family=Bebas+Neue&family=Kurale&family=Montserrat:wght@400;500;700;800&display=swap">
<style>
  :root {
    --sky: #c4e7f4;
    --sky-deep: #bfe3f1;
    --leaf: #a6c33f;
    --cyan: #33c2e2;
    --ink: #151515;
    --white: #ffffff;
    --line: #9fcbd3;
    --stage: #eeeeee;
    --stick: #b4582a;
    --coat: #a9552b;
  }
  * { box-sizing: border-box; margin: 0; padding: 0; }
  html, body { width: 794px; height: 1200px; overflow: hidden; }
  body {
    position: relative;
    background: var(--stage);
    font-family: "Montserrat", sans-serif;
    color: var(--ink);
  }
  .card { position: absolute; left: 61px; width: 662px; overflow: hidden; }
  .abs { position: absolute; }
  .layer-top { z-index: 5; }

  /* ---------- front ---------- */
  .front { top: 121px; height: 441px; background: var(--sky); }
  .club-mark { display: flex; align-items: center; gap: 6px; justify-content: center; }
  .club-mark .dot { width: 12px; height: 12px; border-radius: 50%; background: var(--white); border: 2px solid var(--ink); flex: none; }
  .club-mark .name { font-family: "Montserrat", sans-serif; font-weight: 800; font-size: 13px; color: var(--ink); letter-spacing: .5px; text-transform: uppercase; white-space: nowrap; }
  .front .club-mark { left: 87px; top: 52px; width: 200px; }
  .ribbon { left: 65px; top: 102px; width: 252px; height: 37px; }
  .ribbon-text { left: 65px; top: 111px; width: 252px; text-align: center; font-family: "Bebas Neue", sans-serif; font-size: 19px; color: var(--ink); letter-spacing: .3px; transform: rotate(1.5deg); }
  .headline { font-family: "Bebas Neue", sans-serif; color: var(--ink); text-align: center; line-height: 1; }
  .headline.main { left: 39px; top: 146px; width: 310px; font-size: 66px; }
  .headline.sub { left: 93px; top: 205px; width: 200px; font-size: 46px; }
  .join-btn { left: 123px; top: 250px; width: 134px; height: 24px; background: var(--leaf); color: var(--white); font-family: "Kurale", serif; font-size: 15px; display: flex; align-items: center; justify-content: center; }
  .photo-dog { left: 342px; top: 41px; width: 278px; height: 254px; border-radius: 40% 40% 20% 20%; background: radial-gradient(ellipse at 60% 45%, #b15d2f 0%, #9c4c24 45%, rgba(169,85,43,0) 72%); }
  .photo-sticks { left: 25px; top: 226px; width: 155px; height: 121px; z-index: 2;
    background: linear-gradient(140deg, rgba(180,88,42,0) 30%, rgba(180,88,42,.85) 47%, rgba(143,63,29,.85) 55%, rgba(180,88,42,0) 70%); }

  .how-band { left: 0; top: 326px; width: 662px; height: 87px; background: var(--leaf); z-index: 1; }
  .how-title { left: 30px; top: 345px; font-family: "Bebas Neue", sans-serif; color: var(--ink); line-height: .9; text-align: center; }
  .how-title span { display: block; }
  .how-title .t1 { font-size: 21px; }
  .how-title .t2 { font-size: 30px; }
  .icon-pup { left: 121px; top: 345px; width: 55px; height: 50px; border-radius: 8px; background: linear-gradient(#f3efe8, #d9d2c4); z-index: 3; }
  .icon-cow { left: 301px; top: 360px; width: 58px; height: 34px; border-radius: 8px; background: #1a1a1a; z-index: 3; }
  .icon-box { left: 485px; top: 357px; width: 47px; height: 38px; background: linear-gradient(#d9b57a, #c89c5c); z-index: 3; }
  .step h3 { font-family: "Kurale", serif; font-weight: 400; font-size: 10px; color: var(--ink); margin-bottom: 5px; white-space: nowrap; }
  .step p { font-size: 5.2px; line-height: 1.32; color: var(--ink); }
  .step-joy { left: 188px; top: 342px; width: 96px; }
  .step-cattle { left: 334px; top: 342px; width: 136px; }
  .step-cattle p { margin-left: 33px; width: 102px; }
  .step-ship { left: 528px; top: 342px; width: 110px; }
  .step-ship p { margin-left: 11px; width: 97px; }
  .divider { top: 337px; width: 0; height: 66px; border-left: 1px dotted rgba(255,255,255,.8); z-index: 3; }
  .divider.a { left: 292px; }
  .divider.b { left: 475px; }

  .promo-bar { left: 0; width: 100%; background: var(--cyan); display: flex; align-items: center; z-index: 4; }
  .front .promo-bar { top: 412px; height: 29px; padding-left: 23px; }
  .promo-line { font-size: 11.4px; color: var(--ink); white-space: nowrap; }
  .promo-line b { color: var(--white); font-weight: 700; font-size: 12.5px; }
  .web { display: flex; align-items: center; gap: 6px; color: var(--white); font-weight: 800; white-space: nowrap; }
  .web .globe { width: 19px; height: 19px; border-radius: 50%; background: var(--leaf); display: flex; align-items: center; justify-content: center; }
  .front .web { margin-left: auto; margin-right: 22px; font-size: 16px; }

  /* ---------- back ---------- */
  .back { top: 633px; height: 447px; background: var(--white); }
  .back-panel { left: 0; top: 0; width: 332px; height: 447px; background: var(--sky); }
  .back .club-mark { left: 62px; top: 90px; width: 200px; }
  .offer-lead { left: 0; top: 151px; width: 332px; text-align: center; font-size: 11.2px; letter-spacing: .4px; color: var(--ink); }
  .offer-big { left: 0; top: 168px; width: 332px; text-align: center; font-family: "Bebas Neue", sans-serif; font-size: 74px; line-height: .85; color: var(--leaf); }
  .offer-tail { left: 0; top: 237px; width: 332px; text-align: center; font-size: 15px; letter-spacing: .4px; color: var(--ink); }
  .offer-tail b { font-weight: 800; }
  .icon-pup-small { left: 144px; top: 273px; width: 38px; height: 27px; border-radius: 50% 50% 30% 30%; background: linear-gradient(#f3efe8, #c98a63); z-index: 2; }
  .code-box { left: 92px; top: 298px; width: 140px; height: 67px; border-radius: 8px; background: rgba(160,175,185,.35); text-align: center; padding-top: 11px; }
  .code-box .small { font-size: 9.5px; color: var(--ink); display: block; }
  .code-box .code { font-size: 15px; font-weight: 700; color: var(--white); display: block; margin: 2px 0 3px; letter-spacing: .2px; }
  .back .promo-bar { top: 416px; width: 332px; height: 31px; justify-content: center; }
  .back .web { font-size: 16.5px; }

  .stamp-frame { left: 516px; top: 45px; width: 109px; height: 140px; border: 1px solid var(--line); }
  .stamp-fill { left: 523px; top: 52px; width: 95px; height: 126px; background: var(--leaf); }
  .address-line { left: 360px; width: 265px; height: 0; border-top: 1px solid var(--line); }
</style>
</head>
<body>

<section class="card front">
  <div class="abs club-mark layer-top"><span class="dot"></span><span class="name">Velmora Grove Club</span></div>

  <svg class="abs ribbon" viewBox="0 0 252 37" aria-hidden="true">
    <polygon points="0,4 16,2 236,4 252,7 242,20 250,35 128,30 4,31 12,17" fill="#a6c33f"/>
  </svg>
  <div class="abs ribbon-text layer-top">Top quality &amp; healthy bully sticks</div>

  <div class="abs photo-dog" role="img" aria-label="Photo of a brown dog lying down with a bully stick between its paws"></div>

  <div class="abs how-band"></div>
  <div class="abs photo-sticks" role="img" aria-label="Photo of three bully sticks crossed over each other"></div>

  <div class="abs headline main layer-top">Your dog will</div>
  <div class="abs headline sub layer-top">Beg for more</div>
  <div class="abs join-btn layer-top">Join the club</div>

  <div class="abs how-title layer-top"><span class="t1">How it</span><span class="t2">Works:</span></div>
  <div class="abs icon-pup" role="img" aria-label="Illustration of a cartoon puppy beside a badge speech bubble"></div>

  <div class="abs step step-joy layer-top">
    <h3>doggy joy guarantee</h3>
    <p>You will receive a 12 Pack of bully sticks. You will be charged monthly. You can cancel anytime. No muss, no fuss, no disappointed pups. Discounts vary so please read the details before ordering.</p>
  </div>
  <div class="abs divider a"></div>

  <div class="abs step step-cattle layer-top">
    <h3>sourced from free range cattle</h3>
    <p>Our bully sticks are humanely made without added hormones, antibiotics or steroids. All-natural. No additives or artificial preservatives. Manufactured under industry-leading food safety programs.</p>
  </div>
  <div class="abs icon-cow" role="img" aria-label="Illustration of a black cow silhouette marked premium quality"></div>
  <div class="abs divider b"></div>

  <div class="abs step step-ship layer-top">
    <h3>shipped to your doorstep</h3>
    <p>We ship worldwide and inside the United States; Asia, Africa, North America, South America, Antarctica, Europe, and Australia.</p>
  </div>
  <div class="abs icon-box" role="img" aria-label="Illustration of a taped cardboard shipping box"></div>

  <div class="abs promo-bar">
    <span class="promo-line">Sign up for a subscription &amp; <b>SAVE 50%</b> on your first month</span>
    <span class="web">
      <span class="globe"><svg width="11" height="11" viewBox="0 0 12 12" aria-hidden="true"><circle cx="6" cy="6" r="5" fill="none" stroke="#fff" stroke-width="1.2"/><path d="M1 6h10M6 1c2 2 2 8 0 10M6 1c-2 2-2 8 0 10" fill="none" stroke="#fff" stroke-width="1"/></svg></span>
      www.velmoragroveclub.com
    </span>
  </div>
</section>

<section class="card back">
  <div class="abs back-panel"></div>
  <div class="abs club-mark"><span class="dot"></span><span class="name">Velmora Grove Club</span></div>

  <div class="abs offer-lead">SIGN UP FOR A SUBSCRIPTION &amp;</div>
  <div class="abs offer-big">Save 50%</div>
  <div class="abs offer-tail">ON YOUR <b>FIRST MONTH</b></div>

  <div class="abs icon-pup-small" role="img" aria-label="Illustration of a cartoon puppy peeking over the code box"></div>
  <div class="abs code-box">
    <span class="small">USE CODE:</span>
    <span class="code">VELMORAGROVE</span>
    <span class="small">AT CHECKOUT</span>
  </div>

  <div class="abs promo-bar">
    <span class="web">
      <span class="globe"><svg width="11" height="11" viewBox="0 0 12 12" aria-hidden="true"><circle cx="6" cy="6" r="5" fill="none" stroke="#fff" stroke-width="1.2"/><path d="M1 6h10M6 1c2 2 2 8 0 10M6 1c-2 2-2 8 0 10" fill="none" stroke="#fff" stroke-width="1"/></svg></span>
      www.velmoragroveclub.com
    </span>
  </div>

  <div class="abs stamp-frame"></div>
  <div class="abs stamp-fill"></div>

  <div class="abs address-line" style="top:248px"></div>
  <div class="abs address-line" style="top:284px"></div>
  <div class="abs address-line" style="top:320px"></div>
  <div class="abs address-line" style="top:355px"></div>
  <div class="abs address-line" style="top:393px"></div>
</section>

</body>
</html>
```